1/4 & 1/2 Page Ad For Marketing

Looking to have a ad that we can use for various community advertising requests. We are a wholesale / retail center of landscape supplies. I have attached an aerial photo of our yard some past ad content as well as our new logo designs which is the one with 6 logos which anyone can be used. Would like to be able to use in full color but also black and white.

Industry/Entity Type

Wholesale Retail of Landscape Supplies

Font styles to use
Sans Serif

Colors
59FF00
82FF00
B8FF75
E3FFCB
F4FFEA

Requirements
Must have
• Maple Ridge Depot has a wide variety of decorative stone, mulch, gravel, topsoil and sand products for all your landscaping needs. 920-555-0147 www.mapleridgedepotllc.example

```html
<!DOCTYPE html>
<html lang="en">
<head>
<meta charset="utf-8">
<title>Maple Ridge Depot – Landscaping Materials Supplier</title>
<link rel="stylesheet" href="https://fonts.googleapis.com/css2?family=Anton&family=Outfit:wght@300;500;600;700;800&display=swap">
<style>
  :root{
    --leaf:#7db443;
    --leaf-bright:#66cc22;
    --leaf-deep:#3f9a12;
    --ink:#1d1818;
    --paper:#ffffff;
    --backdrop:#c2c2c2;
    --mulch:#3a2a26;
  }
  html,body{margin:0;padding:0;width:1200px;height:1200px;overflow:hidden;background:var(--backdrop);}
  .ad{position:absolute;left:0;top:175px;width:1200px;height:849px;background:var(--paper);overflow:hidden;font-family:"Outfit",sans-serif;color:var(--ink);}
  .ad-shapes{position:absolute;left:0;top:0;}
  .headline{position:absolute;left:53px;top:76px;margin:0;line-height:1;}
  .headline span{display:block;}
  .headline-lead{font-family:"Anton",sans-serif;font-weight:400;font-size:92px;letter-spacing:-1px;color:var(--ink);line-height:86px;}
  .headline-main{font-family:"Outfit",sans-serif;font-weight:800;font-size:92px;letter-spacing:-2px;color:var(--paper);line-height:80px;}
  .offer-intro{position:absolute;left:78px;top:380px;margin:0;font-size:38px;line-height:44px;letter-spacing:-0.5px;}
  .offer-intro .light{font-weight:300;display:block;}
  .offer-intro .strong{font-weight:800;display:block;}
  .product-list{position:absolute;list-style:none;margin:0;padding:0;font-weight:600;font-size:18px;}
  .product-list li{position:relative;padding-left:26px;white-space:nowrap;}
  .product-list svg{position:absolute;left:0;top:50%;transform:translateY(-50%);}
  .col-a{left:78px;top:505px;}
  .col-a li{height:30.2px;line-height:30px;}
  .col-b{left:413px;top:508px;}
  .col-b li{height:25.9px;line-height:26px;padding-left:32px;}
  .footer{position:absolute;left:0;top:760px;width:1200px;height:60px;}
  .brand{position:absolute;left:78px;top:0;text-align:center;width:232px;}
  .brand-name{display:block;font-weight:600;font-size:26px;letter-spacing:0.5px;line-height:32px;white-space:nowrap;}
  .brand-place{display:block;font-weight:600;font-size:12px;letter-spacing:0.5px;line-height:14px;}
  .phone{position:absolute;left:350px;top:6px;font-weight:700;font-size:34px;line-height:40px;display:flex;align-items:center;gap:8px;}
  .web{position:absolute;left:636px;top:8px;font-weight:500;font-size:30px;line-height:38px;display:flex;align-items:center;gap:10px;white-space:nowrap;}
</style>
</head>
<body>
<main class="ad">
  <svg class="ad-shapes" width="1200" height="849" viewBox="0 0 1200 849">
    <defs>
      <radialGradient id="bed-tones" cx="40%" cy="55%" r="70%">
        <stop offset="0" stop-color="#5a3b36"/>
        <stop offset="0.55" stop-color="#3a2a26"/>
        <stop offset="1" stop-color="#5e5040"/>
      </radialGradient>
      <linearGradient id="nursery-tones" x1="0" y1="0" x2="0" y2="1">
        <stop offset="0" stop-color="#9fd8c0"/>
        <stop offset="0.5" stop-color="#8fb86a"/>
        <stop offset="1" stop-color="#6b9a3e"/>
      </linearGradient>
      <linearGradient id="ribbon" x1="0" y1="0" x2="1" y2="0">
        <stop offset="0" stop-color="#4fb419"/>
        <stop offset="0.5" stop-color="#78dc2a"/>
        <stop offset="1" stop-color="#4fb419"/>
      </linearGradient>
    </defs>
    <!-- green header band -->
    <rect class="header-band" x="0" y="0" width="900" height="397" fill="var(--leaf)"/>
    <!-- white tab -->
    <path class="intro-tab" d="M47 397 V378 Q47 366 59 366 H465 Q477 366 477 378 V397 Z" fill="var(--paper)"/>
    <!-- accent arc under garden photo -->
    <circle cx="994" cy="306" r="409" fill="var(--leaf)"/>
    <!-- garden photo area -->
    <circle cx="992" cy="298" r="405" fill="url(#bed-tones)" role="img" aria-label="Photo of a mulched garden bed with red begonias, caladiums, boulders and a gravel path"/>
    <!-- discount badge -->
    <g class="badge">
      <circle cx="813" cy="633" r="122" fill="var(--leaf-deep)"/>
      <circle cx="813" cy="633" r="113" fill="var(--leaf-bright)"/>
      <circle cx="813" cy="633" r="104" fill="var(--ink)"/>
      <circle cx="813" cy="633" r="100" fill="var(--paper)"/>
      <path d="M668 652 H962 L940 716 H690 Z" fill="url(#ribbon)"/>
      <text x="813" y="645" text-anchor="middle" font-family="Anton, sans-serif" font-size="96" fill="var(--ink)">10%</text>
      <text x="810" y="678" text-anchor="middle" font-family="Outfit, sans-serif" font-weight="800" font-size="26" fill="var(--ink)">EARLY BIRD</text>
      <text x="810" y="706" text-anchor="middle" font-family="Outfit, sans-serif" font-weight="800" font-size="26" fill="var(--ink)">DISCOUNT</text>
    </g>
    <!-- nursery photo -->
    <circle cx="1085" cy="626" r="122" fill="var(--paper)"/>
    <circle cx="1085" cy="626" r="116" fill="url(#nursery-tones)" role="img" aria-label="Photo of a staff member watering plants in a greenhouse nursery"/>
    <symbol id="tick" viewBox="0 0 20 20">
      <circle cx="10" cy="10" r="8" fill="none" stroke="currentColor" stroke-width="1.6" stroke-dasharray="40 10"/>
      <path d="M6 10 L9.2 13 L18 4" fill="none" stroke="currentColor" stroke-width="1.8" stroke-linecap="round" stroke-linejoin="round"/>
    </symbol>
  </svg>

  <h1 class="headline">
    <span class="headline-lead">LANDSCAPING</span>
    <span class="headline-main">MATERIALS</span>
    <span class="headline-main">SUPPLIER</span>
  </h1>

  <h2 class="offer-intro">
    <span class="light">WE OFFER MANY</span>
    <span class="strong">DIFFERENT PRODUCTS:</span>
  </h2>

  <ul class="product-list col-a">
    <li><svg width="20" height="20"><use href="#tick"/></svg>Cedar Mulch</li>
    <li><svg width="20" height="20"><use href="#tick"/></svg>Red, Brown, Gold &amp; Black Mulch</li>
    <li><svg width="20" height="20"><use href="#tick"/></svg>Standard Hardwood</li>
    <li><svg width="20" height="20"><use href="#tick"/></svg>Pine Playground Wood Chips</li>
    <li><svg width="20" height="20"><use href="#tick"/></svg>Soil (Pulverized Topsoil</li>
    <li><svg width="20" height="20"><use href="#tick"/></svg>Compost</li>
    <li><svg width="20" height="20"><use href="#tick"/></svg>Garden Mix</li>
  </ul>

  <ul class="product-list col-b">
    <li><svg width="20" height="20"><use href="#tick"/></svg>Seed</li>
    <li><svg width="20" height="20"><use href="#tick"/></svg>Gravels</li>
    <li><svg width="20" height="20"><use href="#tick"/></svg>Several Different</li>
    <li><svg width="20" height="20"><use href="#tick"/></svg>Types of Decorative Stone</li>
    <li><svg width="20" height="20"><use href="#tick"/></svg>Drain Tile Products</li>
    <li><svg width="20" height="20"><use href="#tick"/></svg>Edging</li>
    <li><svg width="20" height="20"><use href="#tick"/></svg>Flagstone</li>
    <li><svg width="20" height="20"><use href="#tick"/></svg>Landscape Fabrics</li>
  </ul>

  <footer class="footer">
    <div class="brand">
      <span class="brand-name">Maple Ridge Depot</span>
      <span class="brand-place">Maple Ridge, WI</span>
    </div>
    <div class="phone">
      <svg width="28" height="28" viewBox="0 0 24 24" aria-hidden="true"><path d="M6.6 10.8a15 15 0 0 0 6.6 6.6l2.2-2.2a1 1 0 0 1 1-.25 11.4 11.4 0 0 0 3.6.6 1 1 0 0 1 1 1V20a1 1 0 0 1-1 1A17 17 0 0 1 3 4a1 1 0 0 1 1-1h3.5a1 1 0 0 1 1 1c0 1.25.2 2.45.6 3.6a1 1 0 0 1-.25 1Z" fill="var(--leaf)"/><path d="M14 3a7 7 0 0 1 7 7M14 6.5a3.5 3.5 0 0 1 3.5 3.5" fill="none" stroke="var(--leaf)" stroke-width="1.8" stroke-linecap="round"/></svg>
      <span>920-555-0147</span>
    </div>
    <div class="web">
      <svg width="26" height="26" viewBox="0 0 24 24" aria-hidden="true"><circle cx="12" cy="12" r="10" fill="none" stroke="var(--leaf)" stroke-width="2"/><ellipse cx="12" cy="12" rx="4.5" ry="10" fill="none" stroke="var(--leaf)" stroke-width="1.6"/><path d="M2 12h20M4 7h16M4 17h16" stroke="var(--leaf)" stroke-width="1.6"/></svg>
      <span>www.mapleridgedepotllc.example</span>
    </div>
  </footer>
</main>
</body>
</html>
```